Halvern Capital, Inc.

We need a website design for a new company based in Orange County, CA but will be serving client's throughout all of California. We provide non-recourse loans/ pre-litigation funding for client's in personal injury and employment cases. Generally, if a client has an active case and they need money for cost of living, the client will contact a company like ours to provide a loan. We would like to see designs that are sleek, simple and easy to use. The final design should communicate trustworthiness, financial safety and promptness.

Hi, I like TK's designs. I am having him work on a hybrid of two of his designs. We had a little miscommunication, but we are almost there. Best, Ren

```html
<!DOCTYPE html>
<html lang="en">
<head>
<meta charset="utf-8">
<title>Halvern Capital — Website Design</title>
<link href="https://fonts.googleapis.com/css2?family=Montserrat:wght@400;600;700&family=Open+Sans:wght@400;600&family=Lora:ital,wght@0,400;1,400&display=swap" rel="stylesheet">
<style>
:root{
  --gold:#c0975a;
  --gold-dark:#a9814a;
  --ink:#222;
  --muted:#8a8a8a;
  --dark:#1b1b1b;
  --panel:#f6f6f6;
  --line:#e2e2e2;
}
*{box-sizing:border-box;margin:0;padding:0}
html,body{width:1200px;height:1200px;overflow:hidden;background:#fff}
body{position:relative;font-family:"Open Sans",sans-serif;color:var(--ink)}
.page{position:absolute;background:#fff;overflow:hidden;box-shadow:0 0 22px rgba(0,0,0,.18)}
.page-left{left:70px;top:14px;width:509px;height:1186px}
.page-right{left:641px;top:0;width:509px;height:1088px}
.abs{position:absolute}
.fill{position:absolute}
.h{font-family:"Montserrat",sans-serif;font-weight:600;text-transform:uppercase;letter-spacing:.5px}
.center{text-align:center}
.divider{position:absolute;height:1px;width:14px;background:#333;left:50%;margin-left:-7px}
.btn{position:absolute;background:var(--gold);color:#222;font-family:"Montserrat",sans-serif;font-weight:600;font-size:4.6px;letter-spacing:.4px;text-transform:uppercase;display:flex;align-items:center;justify-content:center;gap:3px;white-space:nowrap}
.brand{font-family:"Montserrat",sans-serif;font-weight:600;text-transform:uppercase;color:var(--gold);letter-spacing:.6px;display:flex;align-items:center;gap:4px}
.brand .dot{width:6px;height:6px;border-radius:50%;background:var(--gold)}

/* hero */
.hero{left:0;top:0;width:509px;height:242px;background:linear-gradient(180deg,#6f737c 0%,#9ea2a8 45%,#7d8087 100%)}
.hero-social{left:10px;top:12px;display:flex;gap:7px}
.hero-social span{width:4px;height:4px;background:#ddd;border-radius:1px}
.hero-brand{left:0;width:509px;top:108px;justify-content:center;font-size:9px;color:#fff}
.hero-brand .dot{background:var(--gold);width:9px;height:9px}
.hero-nav{left:0;width:509px;top:164px;display:flex;justify-content:center;gap:11px;font-size:5px;color:#fff}
.hero-nav .active{color:var(--gold)}

/* sticky bar */
.bar{left:0;top:242px;width:509px;height:21px;background:#fff;border-bottom:1.5px solid var(--gold)}
.bar-brand{left:76px;top:7px;font-size:5px}
.bar-nav{left:168px;top:8px;width:170px;display:flex;justify-content:space-between;font-size:3.9px;letter-spacing:.2px;color:#333;white-space:nowrap}
.bar-btn{left:345px;top:4px;width:47px;height:14px;background:var(--dark);color:var(--gold)}

/* about */
.photo-flag{left:72px;top:312px;width:84px;height:140px;background:linear-gradient(180deg,#b6bcc1,#8c9399)}
.photo-statue{left:354px;top:312px;width:84px;height:140px;background:linear-gradient(180deg,#2f9fd8,#5cb7e3 60%,#4c9e9a)}
.about-col{left:175px;width:160px;top:318px}
.about-title{font-size:9px;margin-top:14px}
.about-text{font-size:4.4px;line-height:7.5px;color:#666;margin-top:20px}
.signature{left:225px;top:418px;width:60px;height:22px;background:#f1f1f1}

/* how we do */
.how-img{left:0;top:479px;width:255px;height:197px;background:linear-gradient(135deg,#3b2d22,#6a5139 50%,#2a221b)}
.how-title{left:76px;top:564px;font-family:"Montserrat",sans-serif;font-weight:700;font-size:15px;color:#fff}
.how-list{left:255px;top:479px;width:254px;height:197px;background:var(--panel)}
.feat{position:absolute;left:29px;width:200px}
.feat svg{position:absolute;left:0;top:0}
.feat .h{position:absolute;left:16px;top:0;font-size:4.8px;color:#222}
.feat p{position:absolute;left:16px;top:9px;width:170px;font-size:3.9px;line-height:7px;color:#999}
.up{position:absolute;width:12px;height:12px;background:#ccc;display:flex;align-items:center;justify-content:center}

/* service circles */
.circle{position:absolute;width:88px;height:88px;border-radius:50%;display:flex;align-items:center;justify-content:center;text-align:center;font-family:"Montserrat",sans-serif;font-weight:700;font-size:7.5px;color:#fff;text-transform:uppercase;line-height:11px}
.c-loan{left:85px;top:700px;background:radial-gradient(circle,#d8d4cc,#a9a59c)}
.c-cons{left:210px;top:700px;background:radial-gradient(circle,#8a5a3a,#3a2a20)}
.c-atty{left:336px;top:700px;background:radial-gradient(circle,#c9c7c4,#8e7e6e)}
.tag-low{left:108px;top:702px;background:var(--gold);color:#fff;font-size:3.6px;padding:2px 3px}
.svc-text{position:absolute;width:110px;text-align:center}
.svc-text .tl{font-size:4.8px;color:var(--gold)}
.svc-text p{font-size:3.7px;line-height:6.5px;color:#999;margin-top:6px}
.svc-text .rm{font-family:"Montserrat",sans-serif;font-weight:600;font-size:3.8px;color:var(--gold);margin-top:6px;text-decoration:underline}

/* pricing */
.pricing-bg{left:0;top:872px;width:509px;height:192px;background:linear-gradient(180deg,#3a3f46,#1f2329 55%,#474b52)}
.pricing-title{left:0;width:509px;top:924px;font-size:9px;color:#fff}
.pricing-box{left:67px;top:973px;width:376px;height:198px;background:var(--dark)}
.price-item{position:absolute;width:156px}
.price-item .row{display:flex;justify-content:space-between;border-bottom:1px dotted #444;padding-bottom:1px}
.price-item .n{font-family:"Montserrat",sans-serif;font-size:4.6px;color:var(--gold);text-transform:uppercase;letter-spacing:.4px}
.price-item .v{font-family:"Lora",serif;font-size:6.5px;color:#fff;font-weight:700}
.price-item p{font-size:3.8px;line-height:6.5px;color:#888;margin-top:2px}

/* right page: services */
.svc-title{left:0;width:509px;top:52px;font-size:9px}
.card{position:absolute;top:91px;width:85px;height:88px;border:1px solid #eee;text-align:center}
.card .img{height:56px}
.card .pr{font-size:5px;color:var(--gold);margin-top:8px}
.card .pr s{color:#aaa}
.card .nm{font-size:5.2px;margin-top:4px}
.sale{position:absolute;left:3px;top:4px;background:var(--gold);color:#fff;font-size:3.6px;padding:1px 2px}

/* testimonials */
.testi{left:0;top:236px;width:509px;height:222px;background:radial-gradient(ellipse at 60% 40%,#5a3a22,#2a1c12 60%,#1a120c)}
.testi-title{left:0;width:509px;top:260px;font-size:8px;color:#fff}
.quote{left:155px;width:200px;top:298px;font-family:"Lora",serif;font-style:italic;font-size:5.4px;line-height:9px;color:#fff;text-align:center}
.qmark{font-family:"Lora",serif;font-size:16px;color:var(--gold);position:absolute}
.partner{position:absolute;top:416px;width:14px;height:14px;border-radius:50%;background:rgba(255,255,255,.75)}
.vline{position:absolute;top:400px;width:1px;height:46px;background:rgba(255,255,255,.12)}

/* team */
.team-title{left:0;width:509px;top:461px;font-size:8px}
.team-text{left:170px;width:170px;top:476px;font-size:5px;line-height:9.5px;color:#666}
.member{position:absolute;top:520px;height:142px}
.member-name{position:absolute;top:670px;width:116px;text-align:center;font-size:5.5px}

/* contact */
.map{left:0;top:679px;width:254px;height:191px;background:#e7e5e1}
.contact{left:254px;top:679px;width:255px;height:191px;background:var(--panel)}
.contact .h2{position:absolute;left:20px;top:22px;font-size:7px}
.contact .addr{position:absolute;left:20px;top:42px;font-size:4.1px;line-height:8.5px;color:#555}
.contact .addr2{position:absolute;left:134px;top:42px;font-size:4.1px;line-height:8.5px;color:#555}
.field{position:absolute;border-bottom:1px solid #d7c5a6;font-size:4.4px;color:#b5b5b5;padding-bottom:3px}

/* banner + footer */
.banner{left:0;top:870px;width:509px;height:51px;background:var(--gold);display:flex;align-items:center;justify-content:center;font-family:"Lora",serif;font-size:9.5px;color:#fff}
.banner b{text-decoration:underline;margin-left:3px;font-weight:700}
.footer{left:0;top:921px;width:509px;height:167px;background:var(--dark)}
.footer-brand{left:0;width:509px;top:75px;justify-content:center;font-size:10px}
.footer-brand .dot{width:10px;height:10px}
.footer-social{left:0;width:509px;top:145px;display:flex;justify-content:center;gap:8px}
.footer-social span{width:4px;height:4px;background:#555;border-radius:1px}
.copy{left:0;width:509px;top:160px;font-size:3.6px;color:#3a3a3a;letter-spacing:.5px}
</style>
</head>
<body>

<!-- Left page -->
<section class="page page-left">
  <header class="abs hero" role="img" aria-label="State capitol building with dome and columns"></header>
  <div class="abs hero-social"><span></span><span></span><span></span><span></span></div>
  <div class="btn" style="left:417px;top:8px;width:83px;height:18px">
    <svg width="5" height="5" viewBox="0 0 10 10"><rect x="1" y="2" width="8" height="7" fill="none" stroke="#222" stroke-width="1.2"/></svg>Make an appointment</div>
  <div class="abs brand hero-brand"><span class="dot"></span>Halvern Capital</div>
  <nav class="abs h hero-nav"><span class="active">Home</span><span>Features</span><span>Pricing</span><span>Services</span><span>Testimonial</span><span>Contact</span></nav>

  <div class="abs bar">
    <div class="abs brand bar-brand"><span class="dot" style="width:5px;height:5px"></span>Halvern</div>
    <nav class="abs h bar-nav"><span>Home</span><span>Features</span><span>Pricing</span><span>Services</span><span>Testimonial</span><span>Contact</span></nav>
    <div class="btn bar-btn">Appointment</div>
  </div>

  <div class="fill photo-flag" role="img" aria-label="Flag on a pole against a cloudy sky"></div>
  <div class="fill photo-statue" role="img" aria-label="Statue with raised torch against a blue sky"></div>
  <div class="abs about-col center">
    <svg width="16" height="14" viewBox="0 0 20 18"><g fill="none" stroke="var(--gold)" stroke-width="1.3"><line x1="10" y1="1" x2="10" y2="16"/><line x1="3" y1="4" x2="17" y2="4"/><path d="M1 10 L3 4 L5 10 Z"/><path d="M15 10 L17 4 L19 10 Z"/><line x1="6" y1="16" x2="14" y2="16"/></g></svg>
    <div class="h about-title">About Us</div>
    <div class="about-text">A short description of the company and what services it offers, plus the most important features that set it apart from others. It can also carry some small history from the beginning until now.</div>
  </div>
  <div class="divider" style="top:375px"></div>
  <div class="fill signature" role="img" aria-label="Handwritten signature"></div>

  <div class="fill how-img" role="img" aria-label="Old library hall with tall bookshelves and busts"></div>
  <div class="abs how-title">How We Do</div>
  <div class="abs how-list">
    <div class="feat" style="top:29px"><svg width="10" height="9" viewBox="0 0 20 18"><rect x="1" y="5" width="18" height="12" fill="none" stroke="var(--gold)" stroke-width="1.4"/><rect x="7" y="1" width="6" height="4" fill="none" stroke="var(--gold)" stroke-width="1.4"/></svg><div class="h">Professional Lawyers</div><p>We have a strong team of young lawyers that can help you with your case in any matter.</p></div>
    <div class="feat" style="top:72px"><svg width="10" height="10" viewBox="0 0 20 20"><rect x="1" y="3" width="18" height="16" fill="none" stroke="var(--gold)" stroke-width="1.4"/><line x1="1" y1="8" x2="19" y2="8" stroke="var(--gold)" stroke-width="1.4"/></svg><div class="h">11 Years Experience</div><p>Our company has been in the business for more than a decade and the team has great experience.</p></div>
    <div class="feat" style="top:114px"><svg width="10" height="10" viewBox="0 0 20 20"><path d="M2 14 L8 14 L14 10 M2 18 L12 18 L19 12" fill="none" stroke="var(--gold)" stroke-width="1.4"/><circle cx="14" cy="5" r="3" fill="none" stroke="var(--gold)" stroke-width="1.4"/></svg><div class="h">Loan For Help</div><p>We won't let you face trouble in hard times, we are with you in every single step of your documents.</p></div>
    <div class="feat" style="top:157px"><svg width="10" height="10" viewBox="0 0 20 20"><circle cx="6" cy="5" r="3" fill="none" stroke="var(--gold)" stroke-width="1.4"/><circle cx="14" cy="5" r="3" fill="none" stroke="var(--gold)" stroke-width="1.4"/><path d="M1 18 L1 12 L11 12 L11 18 M9 18 L9 12 L19 12 L19 18" fill="none" stroke="var(--gold)" stroke-width="1.4"/></svg><div class="h">Professional Consultant</div><p>We also offer professional consultant services regarding legal matters.</p></div>
    <div class="feat" style="top:191px"><svg width="10" height="10" viewBox="0 0 20 20"><circle cx="10" cy="10" r="8" fill="none" stroke="var(--gold)" stroke-width="1.4"/></svg><div class="h">Free Quote</div></div>
    <div class="up" style="left:226px;top:182px"><svg width="5" height="4" viewBox="0 0 10 6"><path d="M1 5 L5 1 L9 5" fill="none" stroke="#fff" stroke-width="1.5"/></svg></div>
  </div>

  <div class="circle c-loan" role="img" aria-label="Banknotes and calculator on a desk">Loan</div>
  <div class="abs tag-low">low rate*</div>
  <div class="circle c-cons" role="img" aria-label="Desk with papers and coffee from above">Consultant</div>
  <div class="circle c-atty" role="img" aria-label="Person in suit carrying a briefcase">Attorney<br>Services</div>
  <div class="svc-text" style="left:74px;top:798px"><div class="tl">Your Property in Good Hands.</div><p>Fast funding for active cases with clear terms and no hidden fees for you at any stage.</p><div class="rm">READ MORE</div></div>
  <div class="svc-text" style="left:199px;top:798px"><div class="tl">Construction Process Organized.</div><p>Our advisors guide you through each step so your case plan stays calm and organized.</p><div class="rm">READ MORE</div></div>
  <div class="svc-text" style="left:325px;top:798px"><div class="tl">We have got you Covered.</div><p>We work with attorneys across California to review your case and respond quickly.</p><div class="rm">READ MORE</div></div>

  <div class="fill pricing-bg" role="img" aria-label="Man in a dark suit buttoning his jacket"></div>
  <svg class="abs" style="left:248px;top:902px" width="13" height="11" viewBox="0 0 20 16"><rect x="1" y="3" width="16" height="12" fill="#fff"/><circle cx="15" cy="9" r="3" fill="#333" stroke="#fff"/></svg>
  <div class="abs h center pricing-title">Pricing</div>
  <div class="abs pricing-box">
    <div class="price-item" style="left:27px;top:24px"><div class="row"><span class="n">Case Reading</span><span class="v">$139</span></div><p>A full review of your case file and funding options by our team.</p></div>
    <div class="price-item" style="left:196px;top:24px"><div class="row"><span class="n">Estimate</span><span class="v">FREE</span></div><p>Get a quick estimate of the amount you can receive on your case.</p></div>
    <div class="price-item" style="left:27px;top:67px"><div class="row"><span class="n">Consultant</span><span class="v">$??</span></div><p>Speak with an advisor about the terms and timing of your funding.</p></div>
    <div class="price-item" style="left:196px;top:67px"><div class="row"><span class="n">Questions</span><span class="v">$27/h</span></div><p>Hourly answers to any questions about your contract and payout.</p></div>
    <div class="price-item" style="left:27px;top:119px"><div class="row"><span class="n">Item 7</span><span class="v">$29</span></div><p>Document handling and filing support for your active case.</p></div>
    <div class="price-item" style="left:196px;top:119px"><div class="row"><span class="n">Item 8</span><span class="v">$17</span></div><p>Status updates and follow up calls with your attorney office.</p></div>
    <div class="btn" style="left:26px;top:159px;width:324px;height:18px">
      <svg width="5" height="5" viewBox="0 0 10 10"><rect x="1" y="2" width="8" height="7" fill="none" stroke="#222" stroke-width="1.2"/></svg>Make an appointment</div>
  </div>
</section>

<!-- Right page -->
<section class="page page-right">
  <svg class="abs" style="left:248px;top:32px" width="13" height="11" viewBox="0 0 20 17"><rect x="1" y="4" width="18" height="12" fill="var(--gold)"/><rect x="7" y="1" width="6" height="3" fill="none" stroke="var(--gold)" stroke-width="1.5"/></svg>
  <div class="abs h center svc-title">Services</div>
  <div class="divider" style="top:74px"></div>

  <div class="card" style="left:71px"><div class="img" role="img" aria-label="Curved wall of library bookshelves" style="background:linear-gradient(135deg,#7a5a3a,#c9a06a 50%,#5a4030)"></div><div class="pr">$81.49/h</div><div class="h nm">Case Reading</div></div>
  <div class="card" style="left:165px"><div class="img" role="img" aria-label="Handshake over a desk with documents" style="background:linear-gradient(135deg,#2a2e35,#aab0b8 60%,#e6e6e6)"></div><div class="pr">low rate</div><div class="h nm">Loan</div></div>
  <div class="card" style="left:259px"><div class="img" role="img" aria-label="Man in suit standing on stairs" style="background:linear-gradient(180deg,#3a3d44,#1e2126)"></div><div class="pr">$199.99/h</div><div class="h nm">Consultant</div></div>
  <div class="card" style="left:353px"><div class="img" role="img" aria-label="People in a meeting at a table" style="background:linear-gradient(135deg,#d9d4cc,#2c2f36)"></div><span class="sale">-50%</span><div class="pr"><s>$40</s> $19.49</div><div class="h nm">Questions</div></div>
  <div class="btn" style="left:224px;top:198px;width:61px;height:18px">+ More Services</div>
  <div class="up" style="left:489px;top:216px"><svg width="5" height="4" viewBox="0 0 10 6"><path d="M1 5 L5 1 L9 5" fill="none" stroke="#fff" stroke-width="1.5"/></svg></div>

  <div class="fill testi" role="img" aria-label="Wooden gavel on a desk in warm low light"></div>
  <svg class="abs" style="left:247px;top:238px" width="15" height="14" viewBox="0 0 20 19"><path d="M10 1 L12.6 7 L19 7.5 L14 11.6 L15.6 18 L10 14.5 L4.4 18 L6 11.6 L1 7.5 L7.4 7 Z" fill="var(--gold)"/></svg>
  <div class="abs h center testi-title">Testimonials</div>
  <div class="divider" style="top:281px;background:#aaa"></div>
  <span class="qmark" style="left:143px;top:300px">&ldquo;</span>
  <span class="qmark" style="left:358px;top:300px">&rdquo;</span>
  <div class="abs quote">We were at a dead-end when we met this company. They helped us in emotional and financial ways so we can prepare our case. If you are in our situation I strongly suggest you to give this company a chance. You won't regret it.</div>
  <div class="abs center" style="left:0;width:509px;top:334px;font-family:Montserrat,sans-serif;font-size:5px;color:var(--gold);font-weight:600">&ndash; MARA LIND</div>
  <div class="abs center" style="left:0;width:509px;top:342px;font-size:3.4px;color:#aaa">Legal Inc</div>
  <svg class="abs" style="left:246px;top:357px" width="18" height="4"><circle cx="2" cy="2" r="1.2" fill="#888"/><circle cx="7" cy="2" r="1.2" fill="#888"/><circle cx="12" cy="2" r="1.4" fill="#fff"/></svg>
  <div class="vline" style="left:85px"></div><div class="vline" style="left:169px"></div><div class="vline" style="left:254px"></div><div class="vline" style="left:339px"></div><div class="vline" style="left:424px"></div>
  <div class="partner" style="left:35px"></div><div class="partner" style="left:120px"></div><div class="partner" style="left:205px"></div><div class="partner" style="left:290px"></div><div class="partner" style="left:375px"></div><div class="partner" style="left:459px"></div>

  <div class="abs h center team-title">Meet The Team</div>
  <div class="abs center team-text">Here we can introduce every member of the organization including lawyers and managers and others.</div>
  <div class="divider" style="top:503px"></div>
  <div class="member" style="left:71px;width:116px;background:linear-gradient(180deg,#f2f2f2,#8d8d8d)" role="img" aria-label="Man in a suit seen from behind overlooking a city"></div>
  <div class="member" style="left:197px;width:115px;background:linear-gradient(160deg,#1f3340,#0e1a22)" role="img" aria-label="Seated man in a suit adjusting his watch"></div>
  <div class="member" style="left:322px;width:115px;background:linear-gradient(135deg,#c7c2b8,#6b5a48)" role="img" aria-label="Man in a tweed jacket working on a laptop"></div>
  <div class="h member-name" style="left:71px">Mara Lind</div>
  <div class="h member-name" style="left:197px">Owen Price</div>
  <div class="h member-name" style="left:322px">Elias Ford</div>
  <div class="up" style="left:489px;top:660px"><svg width="5" height="4" viewBox="0 0 10 6"><path d="M1 5 L5 1 L9 5" fill="none" stroke="#fff" stroke-width="1.5"/></svg></div>

  <div class="fill map" role="img" aria-label="Map showing the office location"></div>
  <div class="abs contact">
    <div class="h h2">Our Main Office</div>
    <div class="addr"><b>North America:</b><br>518 Marlow Ave, Suite 11<br>Irvine, CA 92618</div>
    <div class="addr2"><b><u>Phone:</u></b> (1) 949 555 0142<br><b><u>Fax:</u></b> (1) 949 555 0178<br><b><u>Email:</u></b> info@halverncapital.com</div>
    <div class="field" style="left:20px;top:78px;width:106px">Name</div>
    <div class="field" style="left:134px;top:78px;width:106px">Email Address</div>
    <div class="field" style="left:20px;top:99px;width:68px">Phone</div>
    <div class="field" style="left:96px;top:99px;width:144px">Subject</div>
    <div class="field" style="left:20px;top:120px;width:220px">Your Message</div>
    <div class="btn" style="left:20px;top:151px;width:55px;height:18px">Send Message</div>
  </div>

  <div class="abs banner">Book your visit online and save upto <b>25% Discount</b>&nbsp;&rarr;</div>
  <footer class="abs footer">
    <div class="abs brand footer-brand"><span class="dot"></span>Halvern Capital</div>
    <div class="abs footer-social"><span></span><span></span><span></span><span></span><span></span><span></span></div>
    <div class="abs center copy">&copy; HALVERN INC. 2017. ALL RIGHTS RESERVED</div>
    <div class="up" style="left:489px;top:138px;background:none"><svg width="5" height="4" viewBox="0 0 10 6"><path d="M1 5 L5 1 L9 5" fill="none" stroke="#fff" stroke-width="1.5"/></svg></div>
  </footer>
</section>

</body>
</html>
```